Web Design for Independent Pet Supply shop.

Larkfield Critter Depot is a locally owned and operated premium natural pet food store and supply company with 2 thriving retail stores in Bend, Oregon, and a home delivery service. The pet food offered is the best on the market and may be described as “holistic”. Also on offer is a vast selection of toys, training tools, treats, and other supplies, as well as dog washing services that range from "do-it yourself" to "spa." Current site: LarkfieldCritterDepot.com. They need a new, updated and responsive site.
Likes:
Tovmira.com: Natural colors, not loud, pages in motion, simple & clean but very informative.
Dunmoregale.com: Everything in simple big colorful blocks. The specials run across the top and in motion. This site looks very professional but simple. The information is available several different places.
Quillbarrow.com: Again big blocks through out. Very Fun and inviting. Tons of information with videos and recipes and testimonials. Pleasant feel and colors as well.
Dislikes:
Zinvor.com: Looks cheap, hate the colors, very busy and over whelming. Hate the old style header bar going across with options. Too many printed words instead of fun images.
Colors should be "natural" tones, warm and soothing. Deep dark blue and greys with earthy wood color.
Do Not Use: Blue violet, violet, red violet

```html
<!DOCTYPE html>
<html lang="en">
<head>
<meta charset="utf-8">
<title>Larkfield Critter Depot</title>
<link href="https://fonts.googleapis.com/css2?family=Roboto:ital,wght@0,300;0,400;0,500;0,700;1,400&family=Roboto+Condensed:wght@400;700&display=swap" rel="stylesheet">
<style>
:root{
  --orange:#e07b2f;
  --orange-dark:#c9661e;
  --navy:#0b1a33;
  --navy-deep:#050d1f;
  --ink:#2b2b2b;
  --grey:#6f6f6f;
  --light:#f2f2f2;
  --white:#ffffff;
  --wood:#6b3e1c;
  --wood-dark:#3a210d;
}
*{box-sizing:border-box;margin:0;padding:0}
html,body{width:1200px;height:2535px;overflow:hidden}
body{font-family:'Roboto',sans-serif;color:var(--ink);background:var(--white);position:relative}
.abs{position:absolute}
section,header,nav,footer{position:absolute;left:0;width:1200px}

/* header */
.site-header{top:0;height:98px;background:var(--white)}
.brand{left:132px;top:32px;display:flex;align-items:center;gap:12px}
.brand-dot{width:30px;height:30px;border-radius:50%;background:var(--orange)}
.brand-name{font-weight:700;font-size:24px;color:var(--orange-dark);letter-spacing:.3px}
.search{left:857px;top:29px;width:211px;height:39px;border:1px solid #cfcfcf;border-radius:2px}
.search span{position:absolute;left:10px;top:11px;font-size:11px;color:#9a9a9a}
.search svg{position:absolute;right:10px;top:10px}

/* nav */
.main-nav{top:98px;height:55px;background:linear-gradient(var(--navy),var(--navy-deep))}
.main-nav a{position:absolute;top:20px;font-size:13px;font-weight:500;color:var(--white);text-decoration:none;letter-spacing:.2px}
.main-nav svg{position:absolute;top:22px}

/* hero */
.hero{top:153px;height:505px;background:linear-gradient(90deg,#8a6a4f 0%,#7a5436 35%,#6e4322 55%,#5a3417 100%)}
.hero-photo{left:0;top:0;width:620px;height:505px;background:radial-gradient(ellipse at 40% 50%,#b58a5f 0%,#8b6240 50%,rgba(110,67,34,0) 85%)}
.hero h1{left:625px;top:148px;width:520px;font-family:'Roboto Condensed',sans-serif;font-weight:400;font-size:46px;line-height:52px;color:var(--white)}
.hero p{left:627px;top:266px;width:500px;font-size:14px;line-height:24px;color:var(--white)}
.btn{display:inline-block;background:var(--orange);color:var(--white);font-size:12px;font-weight:700;text-transform:uppercase;text-align:center;border-radius:2px}
.hero .btn{position:absolute;left:628px;top:362px;width:115px;height:37px;line-height:37px}
.hero-arrows{left:1130px;top:444px}

/* services */
.services{top:658px;height:440px;background:var(--light);text-align:center}
.section-title{font-weight:300;font-size:28px;color:#333}
.services .section-title{position:absolute;left:0;width:1200px;top:44px}
.services .lead{position:absolute;left:330px;width:540px;top:92px;font-size:15px;line-height:26px;color:var(--orange)}
.service{position:absolute;top:160px;width:320px;height:240px;text-align:center}
.service .icon{height:84px;display:flex;justify-content:center;align-items:flex-end}
.service h3{font-weight:400;font-size:21px;margin-top:18px;color:#333}
.service p{font-size:12.5px;line-height:22px;color:var(--grey);margin:12px auto 0;width:245px}
.service .more{position:absolute;left:0;width:320px;top:222px;font-size:12.5px;color:var(--orange)}

/* pet food */
.pet-food{top:1098px;height:355px;background:var(--white)}
.pet-food h2{position:absolute;left:132px;top:50px;font-weight:400;font-size:27px;color:#333}
.pet-food h4{position:absolute;left:132px;top:92px;font-weight:400;font-size:18px;color:var(--orange)}
.pet-food .copy{position:absolute;left:132px;top:128px;width:540px;font-size:11.5px;line-height:22px;color:var(--grey)}
.pet-food .copy p+p{margin-top:12px}
.pet-food-photo{left:655px;top:20px;width:430px;height:335px;background:radial-gradient(ellipse at 62% 50%,#efe9df 0%,#e3d8c8 45%,#fff 80%)}

/* stories */
.stories{top:1453px;height:389px;background:linear-gradient(90deg,#3b2410 0%,#6b4320 40%,#4a2c12 70%,#2e1a09 100%)}
.story-photo{left:174px;top:64px;width:260px;height:260px;border-radius:50%;border:5px solid var(--orange);background:radial-gradient(circle at 50% 45%,#c9a27a,#7b5634)}
.stories h2{position:absolute;left:482px;top:58px;font-weight:300;font-size:28px;color:var(--white)}
.stories blockquote{position:absolute;left:482px;top:114px;width:540px;font-style:italic;font-size:14.5px;line-height:27px;color:var(--white);text-align:justify}
.stories .who{position:absolute;left:482px;top:270px;color:var(--white)}
.stories .who strong{display:block;font-weight:400;font-size:17px}
.stories .who em{font-size:14px}
.arrow-l{left:70px;top:155px}
.arrow-r{left:1085px;top:155px}

/* contact */
.contact{top:1842px;height:399px;background:var(--white)}
.contact h2{position:absolute;left:129px;top:38px;font-weight:400;font-size:27px;color:#333}
.contact .info{position:absolute;left:129px;top:92px;width:280px}
.contact h5{font-weight:400;font-size:15.5px;color:#333}
.contact .row{display:flex;align-items:center;gap:14px;margin-top:10px;color:var(--grey);font-size:12.5px;line-height:19px}
.contact .row.phone{font-size:18px;color:#333}
.contact .row.top{align-items:flex-start}
.form-title{position:absolute;left:432px;top:42px;font-size:17px;color:#333}
.field{position:absolute;height:45px;border:1px solid #d4d4d4;border-radius:2px;font-size:11px;color:#a4a4a4;padding:14px 18px}
.contact .btn{position:absolute;left:432px;top:309px;width:117px;height:44px;line-height:44px;font-size:14px;font-weight:400}
.contact-photo{left:890px;top:85px;width:310px;height:270px;background:radial-gradient(ellipse at 50% 60%,#d9d6d2 0%,#ecebe9 45%,#fff 78%)}

/* footer */
.site-footer{top:2241px;height:294px;background:linear-gradient(var(--navy),var(--navy-deep));color:var(--white)}
.site-footer h6{font-weight:400;font-size:18px}
.col{position:absolute;top:30px}
.col ul{list-style:none;margin-top:14px}
.col li{font-size:12.5px;line-height:23.5px}
.feed{display:flex;gap:12px;margin-top:20px;width:280px}
.feed+.feed{margin-top:18px}
.feed-thumb{width:84px;height:58px;border-radius:2px;background:linear-gradient(135deg,#d9c3a6,#9a7a5a);flex:none}
.feed b{display:block;font-weight:400;font-size:12.5px;margin-bottom:6px}
.feed span{font-size:11px;line-height:17px}
.social{display:flex;align-items:center;gap:22px;margin-top:16px;font-size:12.5px}
.social+.social{margin-top:9px}
.social i{width:32px;height:32px;border:1px solid var(--white);border-radius:50%}
.copyright{position:absolute;left:132px;top:240px;font-size:12px}
</style>
</head>
<body>

<header class="site-header">
  <div class="abs brand"><span class="brand-dot"></span><span class="brand-name">Larkfield Critter Depot</span></div>
  <div class="abs search"><span>Search Here...</span>
    <svg width="16" height="16" viewBox="0 0 16 16"><circle cx="6.5" cy="6.5" r="4.8" fill="none" stroke="#e07b2f" stroke-width="2"/><line x1="10" y1="10" x2="14.5" y2="14.5" stroke="#e07b2f" stroke-width="2.4"/></svg>
  </div>
</header>

<nav class="main-nav">
  <a style="left:132px">HOME</a>
  <a style="left:212px">EVENTS</a>
  <a style="left:304px">BLOG</a>
  <a style="left:381px">ABOUT</a>
  <svg style="left:432px" width="10" height="8" viewBox="0 0 10 8"><path d="M1 2l4 4 4-4" fill="none" stroke="#fff" stroke-width="1.6"/></svg>
  <a style="left:480px">DOG WASH</a>
  <a style="left:590px">PRODUCTS</a>
  <a style="left:701px">RESOURCES</a>
  <svg style="left:786px" width="10" height="8" viewBox="0 0 10 8"><path d="M1 2l4 4 4-4" fill="none" stroke="#fff" stroke-width="1.6"/></svg>
  <a style="left:828px">LINKS</a>
  <a style="left:908px">CONTACT</a>
</nav>

<section class="hero">
  <div class="abs hero-photo" role="img" aria-label="Photo of a smiling girl lying on a rug beside a golden spaniel"></div>
  <h1 class="abs">Dedicated to a better diet for a healthier pet</h1>
  <p class="abs">The Larkfield Critter Depot Dog Wash attendants are always here to help wash your four-legged friends, and trim their nails...but they are also here to help educate all of us! Nail trims are such an essential routine.</p>
  <a class="btn">Learn More</a>
  <svg class="abs hero-arrows" width="36" height="20" viewBox="0 0 36 20"><path d="M12 2L4 10l8 8M24 2l8 8-8 8" fill="none" stroke="#e07b2f" stroke-width="1.6"/></svg>
</section>

<section class="services">
  <h2 class="section-title">We Provide Best Services</h2>
  <p class="lead">The Larkfield Critter Depot Dog Wash attendants are always here to help wash your four-legged&nbsp; friends, and trim their nails...</p>

  <div class="service" style="left:115px">
    <div class="icon"><svg width="80" height="76" viewBox="0 0 80 76" fill="#e07b2f"><ellipse cx="40" cy="54" rx="20" ry="17"/><ellipse cx="24" cy="22" rx="8" ry="11"/><ellipse cx="56" cy="22" rx="8" ry="11"/><ellipse cx="9" cy="40" rx="7" ry="9"/><ellipse cx="71" cy="40" rx="7" ry="9"/></svg></div>
    <h3>Pup Brew</h3>
    <p>Now you can&nbsp; pour some cold brew for your pup in a fun and easy way that has a delicious flavor and packed..</p>
    <span class="more">Read More &gt;</span>
  </div>

  <div class="service" style="left:440px">
    <div class="icon"><svg width="116" height="72" viewBox="0 0 116 72"><path d="M22 24h72l14 40H8z" fill="#e07b2f"/><path d="M42 18a16 14 0 0132 0z" fill="#e07b2f"/><rect x="4" y="62" width="108" height="8" rx="3" fill="#e07b2f"/><path d="M44 40h28" stroke="#fff" stroke-width="7" stroke-linecap="round"/><circle cx="43" cy="36" r="4" fill="#fff"/><circle cx="43" cy="44" r="4" fill="#fff"/><circle cx="73" cy="36" r="4" fill="#fff"/><circle cx="73" cy="44" r="4" fill="#fff"/></svg></div>
    <h3>Nutrivale Lawsuit</h3>
    <p>Nutrivale is being sued by , Dale Morrow of Harlow Cove, Oregon. He he first purchased Kibblecrest food...</p>
    <span class="more">Read More &gt;</span>
  </div>

  <div class="service" style="left:766px">
    <div class="icon"><svg width="70" height="74" viewBox="0 0 70 74"><rect x="4" y="4" width="46" height="46" rx="10" fill="#e07b2f"/><circle cx="46" cy="52" r="18" fill="#e07b2f" stroke="#f2f2f2" stroke-width="3"/><path d="M37 52l6 6 12-12" fill="none" stroke="#fff" stroke-width="4"/></svg></div>
    <h3>Tidewell 5/8" Leads On Sale</h3>
    <p>Your local Tidewell has ALL of their 5/8" Leads ON SALE for just $10!...</p>
    <span class="more">Read More &gt;</span>
  </div>
</section>

<section class="pet-food">
  <h2>Pet Food</h2>
  <h4>The Larkfield Critter Depot Dog Wash News and Updates</h4>
  <div class="copy">
    <p>The Larkfield Critter Depot Dog Wash attendants are always here to help wash your four-legged friends, and trim their nails...but they are also here to help educate all of us! Nail trims are such an essential routine for our pups, especially if they don't run and walk as much as they would in the wild.</p>
    <p>Notice how "cat like" the toes are, tight and together allowing the pads full access to the ground in a healthy way. Dog toe/foot pads relay information to the dog like where the ground is, what angle the slope/stairs are, etc. When toes get twisted due to long nails, signals get mixed and dogs start trying to compensate by standing differently resulting in more strain in their skeletal structure.</p>
  </div>
  <div class="abs pet-food-photo" role="img" aria-label="Photo of a white terrier beside a bowl of dry kibble"></div>
</section>

<section class="stories">
  <svg class="abs arrow-l" width="46" height="80" viewBox="0 0 46 80"><path d="M40 4L6 40l34 36" fill="none" stroke="#e6d6c4" stroke-width="1.5"/></svg>
  <div class="abs story-photo" role="img" aria-label="Photo of a man sitting with a brown dog"></div>
  <h2>Our Success Stories</h2>
  <blockquote>Sed ut perspiciatis unde omnis iste natus error sit voluptatem accusantium doloremque laudantium, totam rem aperiam, eaque ipsa quae ab illo inventore et quasi architecto beatae vitae dicta sunt explicabo. Nemo enim ipsam voluptatem quia voluptas sit aut odit aut fugit, sed quia consequuntur magni dolores eos qui ratione voluptatem sequi nesciunt modi tempora incidunt .</blockquote>
  <div class="who"><strong>Owen Hale,</strong><em>Manager, Company name</em></div>
  <svg class="abs arrow-r" width="46" height="80" viewBox="0 0 46 80"><path d="M6 4l34 36L6 76" fill="none" stroke="#e6d6c4" stroke-width="1.5"/></svg>
</section>

<section class="contact">
  <h2>Contact us</h2>
  <div class="info">
    <h5>Contact for additional information :</h5>
    <div class="row phone"><svg width="14" height="14" viewBox="0 0 14 14"><path d="M3 1l2.5 3-1.5 1.6c.8 1.8 2 3 3.8 3.8L9.4 8 12.6 10.4 11 13C5.5 12.5 1.5 8.5 1 3z" fill="#e07b2f"/></svg>123 456 7890</div>
    <div class="row"><svg width="14" height="11" viewBox="0 0 14 11"><rect width="14" height="11" rx="1" fill="#e07b2f"/><path d="M1 2l6 4 6-4" fill="none" stroke="#fff" stroke-width="1.2"/></svg>info@larkfieldcritterdepot.com</div>
    <h5 style="margin-top:28px">Location &amp; Time :</h5>
    <div class="row" style="margin-top:16px"><svg width="12" height="16" viewBox="0 0 12 16"><path d="M6 16S0 9 0 6a6 6 0 0112 0c0 3-6 10-6 10z" fill="#e07b2f"/><circle cx="6" cy="6" r="2.2" fill="#fff"/></svg>We are loacted at lorem ipsum,2345</div>
    <div class="row top"><svg width="13" height="13" viewBox="0 0 13 13" style="margin-top:3px"><circle cx="6.5" cy="6.5" r="5.5" fill="none" stroke="#e07b2f" stroke-width="1.8"/><path d="M6.5 3.5v3.3l2 1.4" fill="none" stroke="#e07b2f" stroke-width="1.5"/></svg>Open from 9 a.m to 10 p.m on<br>Weekdays</div>
  </div>

  <p class="form-title">Enter your details below &amp; Contact us :</p>
  <div class="field" style="left:432px;top:85px;width:220px">Name</div>
  <div class="field" style="left:664px;top:85px;width:220px">Email</div>
  <div class="field" style="left:432px;top:146px;width:220px">Phone number</div>
  <div class="field" style="left:664px;top:146px;width:220px">Subject</div>
  <div class="field" style="left:432px;top:206px;width:452px;height:83px">Subject</div>
  <a class="btn">SUBMIT</a>

  <div class="abs contact-photo" role="img" aria-label="Photo of a grey cat and a husky sitting together"></div>
</section>

<footer class="site-footer">
  <div class="col" style="left:129px"><h6>Information</h6>
    <ul><li>Home</li><li>Event</li><li>Blog</li><li>About</li><li>Dog Wash</li></ul></div>
  <div class="col" style="left:336px"><h6>Policies</h6>
    <ul><li>Contact</li><li>Return Policy</li><li>Privacy Policy</li><li>Employment</li><li>Staff Login</li></ul></div>
  <div class="col" style="left:533px"><h6>Pawbook Feed</h6>
    <div class="feed"><div class="feed-thumb" role="img" aria-label="Photo of a child with a puppy"></div><div><b>2 people recommended this</b><span>Sed ut perspiciatis unde omnis iste natus error sit</span></div></div>
    <div class="feed"><div class="feed-thumb" role="img" aria-label="Photo of a woman hugging a dog"></div><div><b>2 people recommended this</b><span>Sed ut perspiciatis unde omnis iste natus error sit</span></div></div>
  </div>
  <div class="col" style="left:895px"><h6>Follow us</h6>
    <div class="social"><i></i>Pawbook</div>
    <div class="social"><i></i>Chirpline</div>
    <div class="social"><i></i>Linkwell</div>
    <div class="social"><i></i>Circlewave</div>
  </div>
  <p class="copyright">Copyright © 2015 Larkfield Critter Depot All rights reserved.</p>
</footer>

</body>
</html>
```